Print design needed to improve the layout and look of some existing documents

We need someone to take a couple of existing documents that we have and make them look much better using our existing logo and corporate colors etc. We require these to be delivered in a format that will allow our staff to edit the content as necessary via Microsoft word for conversion once finalized into a PDF. Ideally, we will also be able to use this as a newsletter template or for other documents that might be required in our business. www.larchfieldcapital.com.au
Updates

Project Deadline Extended Reason: So far, I have only seen one design that I believe is quite good quality. Added Sunday, July 3, 2016

Target Market(s)

Business owners, executives, retirees

Industry/Entity Type

Financial Service

Font styles to use
Serif

Requirements
Must have
• Design that uses our existing branding and colors. It also needs to be ina form that we can edit the content / update easily. Ideally the format / layout could also be used for other documents such as short newsletters etc.
Nice to have
• Fresh, simple and crisp. Very professional looking.
Should not have
• strange fonts, weird layouts.

```html
<!DOCTYPE html>
<html lang="en">
<head>
<meta charset="utf-8">
<title>Larchfield Capital – Financial Services Guide, page 5</title>
<link rel="stylesheet" href="https://fonts.googleapis.com/css2?family=Nunito:ital,wght@0,400;0,800;1,300;1,400&display=swap">
<style>
  :root {
    --brand-blue: #1b9ad8;
    --brand-green: #6db446;
    --brand-navy: #1d3e7a;
    --edge-top: #45ace0;
    --edge-bottom: #6cb447;
    --ink: #2b2b2b;
    --paper: #ffffff;
  }
  html, body {
    margin: 0;
    padding: 0;
    overflow: hidden;
    background: var(--paper);
  }
  .page {
    position: relative;
    width: 831px;
    height: 1200px;
    overflow: hidden;
    background: var(--paper);
    font-family: "Nunito", sans-serif;
    color: var(--ink);
  }
  .edge-band {
    position: absolute;
    top: 0;
    right: 0;
    width: 29px;
    height: 1200px;
    background: linear-gradient(to bottom, var(--edge-top), var(--edge-bottom));
  }
  .section-tab {
    position: absolute;
    left: 11px;
    width: 229px;
    height: 51px;
  }
  .section-tab svg {
    position: absolute;
    inset: 0;
  }
  .section-tab h2 {
    position: relative;
    margin: 0;
    padding-left: 9px;
    height: 100%;
    display: flex;
    align-items: center;
    font-weight: 800;
    font-size: 17.5px;
    line-height: 19px;
    color: #fff;
  }
  .copy {
    position: absolute;
    width: 364px;
    margin: 0;
    font-style: italic;
    font-weight: 400;
    font-size: 13.6px;
    line-height: 19.8px;
    text-align: justify;
    text-align-last: left;
  }
  .col-left { left: 20px; }
  .col-right { left: 417px; }
  .bullets {
    position: absolute;
    left: 417px;
    width: 364px;
    margin: 0;
    padding: 0;
    list-style: none;
    font-style: italic;
    font-size: 13.6px;
    line-height: 19.8px;
  }
  .bullets li {
    position: relative;
    padding-left: 10px;
  }
  .bullets li::before {
    content: "";
    position: absolute;
    left: 1px;
    top: 8px;
    width: 5px;
    height: 5px;
    border-radius: 50%;
    background: var(--brand-blue);
  }
  .page-number {
    position: absolute;
    left: 691px;
    top: 1158px;
    font-size: 17px;
    color: #333;
  }
</style>
</head>
<body>
<div class="page">
  <div class="edge-band"></div>

  <!-- Left column -->
  <div class="section-tab" style="top:30px">
    <svg width="229" height="51" viewBox="0 0 229 51"><rect width="229" height="51" fill="var(--brand-blue)"/><path d="M180 0 H222 Q229 0 229 7 V51 Z" fill="var(--brand-green)"/><path d="M180 0 L229 51" stroke="var(--brand-navy)" stroke-width="5"/></svg>
    <h2>Referral Fees and<br>Commissions</h2>
  </div>
  <p class="copy col-left" style="top:101px">In some situations we may receive fees or commissions when we refer you to external parties.<br>We will disclose the referral arrangements to you whenever we refer you to an external party.</p>
  <p class="copy col-left" style="top:200px">In some situations we may pay fees or commissions to external parties who have referred you to us. We will disclose the referral arrangements to you when we provide you with a SoA.</p>

  <div class="section-tab" style="top:303px">
    <svg width="229" height="51" viewBox="0 0 229 51"><rect width="229" height="51" fill="var(--brand-blue)"/><path d="M180 0 H222 Q229 0 229 7 V51 Z" fill="var(--brand-green)"/><path d="M180 0 L229 51" stroke="var(--brand-navy)" stroke-width="5"/></svg>
    <h2>Conflicts of Interest</h2>
  </div>
  <p class="copy col-left" style="top:379px">We may hold investments we recommend Martin Hale, Peter Varga and Neil Ashcombe may provide advice on investments which they hold or may hold in their own personal portfolios.</p>
  <p class="copy col-left" style="top:479px">We will disclose the size and nature of these holdings where there may be a conflict of interest with the advice that we provide.</p>

  <div class="section-tab" style="top:562px">
    <svg width="229" height="51" viewBox="0 0 229 51"><rect width="229" height="51" fill="var(--brand-blue)"/><path d="M180 0 H222 Q229 0 229 7 V51 Z" fill="var(--brand-green)"/><path d="M180 0 L229 51" stroke="var(--brand-navy)" stroke-width="5"/></svg>
    <h2>Making a Complaint</h2>
  </div>
  <p class="copy col-left" style="top:639px">We will endeavour to provide you with the best advice and service at all times.</p>
  <p class="copy col-left" style="top:699px">If for any reason you are not satisfied with our services we encourage you to contact us and to put your complaint in writing.</p>
  <p class="copy col-left" style="top:778px">If you are not satisfied with our response you can refer it to the Financial Disputes Service (FDS).<br>You can contact FDS on 1300 555 214.<br>This service is available to you free of charge.</p>

  <div class="section-tab" style="top:882px">
    <svg width="229" height="51" viewBox="0 0 229 51"><rect width="229" height="51" fill="var(--brand-blue)"/><path d="M180 0 H222 Q229 0 229 7 V51 Z" fill="var(--brand-green)"/><path d="M180 0 L229 51" stroke="var(--brand-navy)" stroke-width="5"/></svg>
    <h2>Your Privacy</h2>
  </div>
  <p class="copy col-left" style="top:956px">Larchfield Capital is committed to protecting your privacy. We have a Privacy Policy which sets out how we collect, hold, use and disclose your personal information.</p>

  <!-- Right column -->
  <p class="copy col-right" style="top:38px">We will collect personal information from you so that we can understand your personal situation and provide you with advice which meets your needs and objectives.</p>
  <p class="copy col-right" style="top:117px">We will also collect information from you to meet our obligations under the Anti-Money Laundering and Counter-Terrorism Financing Act.<br>We will generally collect this information directly from you. However in some cases we will seek your authority to collect if from other parties such as your accountant or your superannuation fund.</p>
  <p class="copy col-right" style="top:277px">If you do not provide us with all of the information that we request, we may not be able to provide our services to you.</p>
  <p class="copy col-right" style="top:357px">We will hold and use your personal information so that we can continue to provide our services to you.</p>
  <p class="copy col-right" style="top:417px">We will only disclose your personal information to external parties where:</p>
  <ul class="bullets" style="top:476px">
    <li>The law requires us to do so</li>
    <li>You consent for us to do so</li>
    <li>You direct us to provide information to other professional services providers such as your Accountant or Lawyer.</li>
  </ul>
  <p class="copy col-right" style="top:596px">Our Privacy Policy contains further information on how we collect, hold, use and disclose your personal information. It also sets out how you can access the information we hold about you, how to have it corrected and how to complain where you are not satisfied with how we have handled your personal information.</p>
  <p class="copy col-right" style="top:737px">Our full Privacy Policy is available on our website.</p>

  <div class="page-number">Page 5 of 6</div>
</div>
</body>
</html>
```